Product packaging design for lentils

Looking to create a design for lentils in 4lb format. We are looking to create a base design for the bags, and then from there will have additional designs for the different products with different product name, barcodes and nutritional information.

Industry/Entity Type

Food

```html
<!DOCTYPE html>
<html lang="en">
<head>
<meta charset="utf-8">
<title>Red Split Lentils – 4lb Bag</title>
<link rel="stylesheet" href="https://fonts.googleapis.com/css2?family=Roboto:wght@400;500;700;900&family=Roboto+Condensed:wght@700&family=Playball&display=swap">
<style>
  :root {
    --backdrop: #ece8e2;
    --bag-red: #9e1012;
    --bag-red-dark: #6f0a0b;
    --bag-red-light: #b8191b;
    --gold: #d9b46a;
    --gold-soft: #e8cf97;
    --lentil-light: #f7923a;
    --lentil-mid: #ee6a22;
    --lentil-deep: #d9501c;
    --badge-green: #1f7a2c;
    --badge-green-dark: #145a1e;
    --badge-yellow: #ffd21a;
    --ink: #1b1b1b;
    --white: #ffffff;
    --brand-ink: #6f0a0b;
  }
  * { box-sizing: border-box; margin: 0; padding: 0; }
  html, body {
    width: 1186px; height: 1200px; overflow: hidden;
    background: var(--backdrop);
    font-family: "Roboto", Arial, sans-serif;
  }
  .bag {
    position: absolute; left: 213px; top: 104px;
    width: 760px; height: 992px;
    background: var(--bag-red);
    overflow: hidden;
    box-shadow: 0 18px 40px rgba(0,0,0,.22);
  }
  .bag__window {
    position: absolute; left: 0; top: 150px; width: 760px; height: 700px;
    background: radial-gradient(ellipse at 45% 45%, var(--lentil-light) 0%, var(--lentil-mid) 55%, var(--lentil-deep) 100%);
  }
  .bag__top {
    position: absolute; left: 0; top: 0; width: 760px; height: 210px;
  }
  .bag__seal-strip {
    position: absolute; left: 0; top: 0; width: 100%; height: 34px;
    background: var(--bag-red-dark);
  }
  .reseal-note {
    position: absolute; left: 0; top: 84px; width: 100%;
    display: flex; align-items: center; justify-content: center; gap: 10px;
    color: rgba(255,255,255,.85); font-size: 17px; letter-spacing: .2px;
  }
  .reseal-note::before, .reseal-note::after {
    content: ""; flex: 0 0 70px; height: 4px;
    border-top: 1px dashed var(--gold); border-bottom: 1px dashed var(--gold);
  }
  .brand {
    position: absolute; left: 0; top: 214px; width: 100%;
    display: flex; align-items: center; justify-content: center; gap: 12px;
  }
  .brand__dot {
    width: 26px; height: 26px; border-radius: 50%; background: var(--badge-green);
  }
  .brand__name {
    font-weight: 900; font-size: 40px; color: var(--brand-ink);
  }
  .quality-seal {
    position: absolute; left: 330px; top: 336px; width: 100px; height: 100px;
    border-radius: 50%;
    background: radial-gradient(circle at 50% 40%, #2f6fb0, #0e2d55 75%);
    border: 4px solid var(--gold);
    z-index: 3;
  }
  .label {
    position: absolute; left: 156px; top: 404px; width: 448px; height: 300px;
    z-index: 2;
  }
  .label svg { position: absolute; inset: 0; }
  .label__script {
    position: absolute; top: 44px; width: 100%; text-align: center;
    font-family: "Playball", cursive; font-size: 44px; color: var(--gold-soft);
  }
  .label__rule {
    position: absolute; left: 60px; width: 328px; height: 1px; background: var(--gold);
  }
  .label__rule::after {
    content: ""; position: absolute; left: 50%; top: -4px; width: 8px; height: 8px;
    background: var(--gold); transform: translateX(-50%) rotate(45deg);
  }
  .label__title {
    position: absolute; top: 124px; width: 100%; text-align: center;
    font-weight: 700; font-size: 58px; color: var(--white); letter-spacing: .5px;
  }
  .label__subtitle {
    position: absolute; top: 202px; width: 100%; text-align: center;
    font-weight: 400; font-size: 34px; color: var(--white);
  }
  .label__weight {
    position: absolute; top: 252px; width: 100%; text-align: center;
    font-weight: 700; font-size: 20px; color: var(--white);
  }
  .bag__bottom {
    position: absolute; left: 0; top: 848px; width: 100%; height: 144px;
    background: var(--bag-red);
    border-top: 3px solid var(--gold);
  }
  .claims {
    position: absolute; left: 0; top: 806px; width: 100%;
    display: flex; justify-content: center; align-items: center; gap: 14px;
    z-index: 3;
  }
  .claim-box {
    width: 62px; height: 80px; border-radius: 8px;
    background: var(--ink); border: 3px solid var(--badge-yellow);
    display: flex; flex-direction: column; align-items: center; overflow: hidden;
    color: var(--white);
  }
  .claim-box__title { font-family: "Roboto Condensed", sans-serif; font-size: 15px; margin-top: 5px; }
  .claim-box__sub { font-size: 8px; }
  .claim-box__value {
    margin-top: auto; width: 100%; height: 34px; background: var(--badge-yellow);
    color: var(--ink); text-align: center;
    font-family: "Roboto Condensed", sans-serif; font-size: 26px; line-height: 34px;
  }
  .claim-circle {
    width: 76px; height: 76px; border-radius: 50%;
    background: var(--badge-green); border: 3px solid var(--white);
    box-shadow: 0 0 0 2px var(--badge-green-dark);
    display: flex; flex-direction: column; align-items: center; justify-content: center;
    color: var(--white); text-align: center; line-height: 1.05;
  }
  .claim-circle__big { font-weight: 900; font-size: 15px; }
  .claim-circle__small { font-weight: 700; font-size: 8px; }
</style>
</head>
<body>
  <div class="bag">
    <div class="bag__window" role="img" aria-label="Photograph of red split lentils filling the bag"></div>

    <div class="bag__top">
      <svg width="760" height="210" viewBox="0 0 760 210">
        <path d="M0 0 H760 V150 Q380 200 0 150 Z" fill="var(--bag-red)"/>
        <path d="M0 150 Q380 200 760 150" fill="none" stroke="var(--gold)" stroke-width="3"/>
      </svg>
      <div class="bag__seal-strip"></div>
      <p class="reseal-note">Resealable for Freshness | Refermable Fraîcheur Garantie</p>
    </div>

    <div class="brand">
      <span class="brand__dot"></span>
      <span class="brand__name">Harvestleaf</span>
    </div>

    <div class="quality-seal"></div>

    <div class="label">
      <svg width="448" height="300" viewBox="0 0 448 300">
        <path d="M40 0 H408 A40 40 0 0 0 448 40 V260 A40 40 0 0 0 408 300 H40 A40 40 0 0 0 0 260 V40 A40 40 0 0 0 40 0 Z" fill="var(--bag-red)"/>
        <path d="M46 10 H402 A36 36 0 0 0 438 46 V254 A36 36 0 0 0 402 290 H46 A36 36 0 0 0 10 254 V46 A36 36 0 0 0 46 10 Z" fill="none" stroke="var(--gold)" stroke-width="3"/>
      </svg>
      <p class="label__script">Red Split Lentils</p>
      <span class="label__rule" style="top:112px"></span>
      <h1 class="label__title">MASOOR DAL</h1>
      <span class="label__rule" style="top:192px"></span>
      <p class="label__subtitle">SPLIT MASUR ROUGE</p>
      <p class="label__weight">NET WT&nbsp; 4LB 1.81KG</p>
    </div>

    <div class="bag__bottom"></div>

    <div class="claims">
      <div class="claim-box">
        <span class="claim-box__title">Fiber</span>
        <span class="claim-box__sub">Per Serving</span>
        <span class="claim-box__value">05g</span>
      </div>
      <div class="claim-circle"><span class="claim-circle__big">100%</span><span class="claim-circle__small">VEGAN</span></div>
      <div class="claim-circle"><span class="claim-circle__big">100%</span><span class="claim-circle__small">NATURAL</span></div>
      <div class="claim-circle"><span class="claim-circle__big">NO</span><span class="claim-circle__small">ADDITIVES</span></div>
      <div class="claim-box">
        <span class="claim-box__title">Protein</span>
        <span class="claim-box__sub">Per Serving</span>
        <span class="claim-box__value">10g</span>
      </div>
    </div>
  </div>
</body>
</html>
```